New cool to-go cup for KELMO Coffee

UPDATE MARCH 18: Please read the attached document "Design ideas - Front" with a mock-up of the design we are looking for. And please don't change the logo.

We are looking for a new cool design for our to-go cups in kraft paper (same style as the attached photo).

The idea:

We have three different cups sizes: 6oz, 8oz and 12oz. We call them “Tiny-Lark” (6oz), “Mid-Wren” (8oz) and “Tall-heron” (12oz) (refers to the size in milliliters). We would like to include this in the cup design. Please see the attached sketch of the idea ("Design ideas - Front").

The backside of the cup should have the attached text and logo ("Design ideas - Back").

But other ideas are also very welcome too! Maybe just a simple cup with the logo.

Please keep the design very minimalistic. The more simple the better.

Target Market(s)

Young urban people

Industry/Entity Type

Coffee shop

Font styles to use
Sans Serif

Requirements
Must have
• Kraft paper cups

```html
<!DOCTYPE html>
<html lang="en">
<head>
<meta charset="utf-8">
<title>KELMO Coffee – To-go Cup</title>
<link rel="stylesheet" href="https://fonts.googleapis.com/css2?family=Montserrat:wght@400;500;600&family=Marcellus&display=swap">
<style>
  :root {
    --backdrop: #3b220e;
    --kraft: #c09068;
    --kraft-shade: #b3845d;
    --rim: #f4f1ec;
    --ink: #2a160b;
  }
  html, body {
    margin: 0;
    padding: 0;
    width: 1200px;
    height: 1200px;
    overflow: hidden;
    background: var(--backdrop);
  }
  .stage { display: block; width: 1200px; height: 1200px; }
  .rim { fill: var(--rim); }
  .cup-wall { fill: url(#kraftTone); }
  .brand-ring { fill: none; stroke: var(--ink); stroke-width: 3.5; }
  .brand-name {
    font-family: "Montserrat", sans-serif;
    font-weight: 600;
    fill: var(--ink);
    letter-spacing: 1px;
  }
  .story-text {
    font-family: "Montserrat", sans-serif;
    font-weight: 400;
    font-size: 21px;
    fill: var(--ink);
  }
  .web-address {
    font-family: "Marcellus", serif;
    font-size: 29px;
    letter-spacing: 2px;
    fill: var(--ink);
    font-weight: 600;
  }
  .social-handle {
    font-family: "Montserrat", sans-serif;
    font-size: 24px;
    letter-spacing: 1px;
    fill: var(--ink);
  }
  .size-name {
    font-family: "Montserrat", sans-serif;
    font-weight: 500;
    fill: var(--ink);
  }
</style>
</head>
<body>
<svg class="stage" viewBox="0 0 1200 1200" xmlns="http://www.w3.org/2000/svg">
  <defs>
    <linearGradient id="kraftTone" x1="0" y1="0" x2="1" y2="0">
      <stop offset="0" stop-color="#b08158"/>
      <stop offset="0.45" stop-color="#c4956c"/>
      <stop offset="1" stop-color="#b5865e"/>
    </linearGradient>
  </defs>

  <!-- Back of the cup -->
  <g class="cup cup-back">
    <path class="rim" d="M136 755 H556 L554 806 Q345 814 138 806 Z"/>
    <path class="cup-wall" d="M62 132 H622 L570 762 Q345 772 124 762 Z"/>
    <rect class="rim" x="48" y="98" width="590" height="38" rx="12"/>

    <g class="brand-mark">
      <circle class="brand-ring" cx="330" cy="330" r="72"/>
      <text class="brand-name" x="330" y="326" font-size="19" text-anchor="middle">KELMO</text>
      <text class="brand-name" x="330" y="350" font-size="14" text-anchor="middle">Coffee</text>
    </g>

    <text class="story-text" text-anchor="middle">
      <tspan x="331" y="459">Read about your coffee</tspan>
      <tspan x="331" y="489">and the dedicated formers</tspan>
      <tspan x="331" y="520">who made this cup possible:</tspan>
    </text>
    <text class="web-address" x="331" y="571" text-anchor="middle">www.kelmocoffee.com</text>
    <text class="social-handle" x="331" y="622" text-anchor="middle">@kelmocoffee</text>
  </g>

  <!-- Front of the cup -->
  <g class="cup cup-front">
    <path class="rim" d="M688 1085 H1076 L1074 1140 Q880 1147 690 1140 Z"/>
    <path class="cup-wall" d="M620 515 H1140 L1088 1092 Q880 1102 682 1092 Z"/>
    <rect class="rim" x="606" y="482" width="546" height="38" rx="12"/>

    <g class="brand-mark">
      <circle class="brand-ring" cx="879" cy="772" r="69"/>
      <text class="brand-name" x="879" y="768" font-size="18" text-anchor="middle">KELMO</text>
      <text class="brand-name" x="879" y="791" font-size="13" text-anchor="middle">Coffee</text>
    </g>

    <text class="size-name" x="879" y="903" font-size="56" text-anchor="middle">tiny lark</text>
    <text class="size-name" x="885" y="1080" font-size="13" text-anchor="middle">tiny lark</text>
  </g>
</svg>
</body>
</html>
```